Willow Ridge Coffee Company Label

I am in need of a label for my coffee brand. I've attached my logo, and the label I've composed in the past. This brand has not launched yet, but we will launch within the week. I'm trying to identify other label options. I am familiar with Adobe Illustrator, enough to design what I have. What I'd like is a logo that is scalable, meaning I can easily change the name of the coffee. For consistency I'd like all of my roasts to have the same label, just different names and descriptions. I've included specs for the label, I'll be using the 3x4 labels for 16 oz bags. When you submit your design please follow the specs. There needs to be my company name and address on the label, however I don't want it to take over the label.

Please reply with any questions or clarifications.

Thank you,

Ned

```html
<!DOCTYPE html>
<html lang="en">
<head>
<meta charset="utf-8">
<title>Willow Ridge Coffee Co. – Long Drive Blend Label</title>
<link href="https://fonts.googleapis.com/css2?family=Cormorant+SC:wght@500;600;700&family=Lato:wght@400&display=swap" rel="stylesheet">
<style>
  :root{
    --page:#f4f4f4;
    --roast:#4a2612;
    --paper:#ececee;
    --paper-edge:#dedee2;
    --ink:#1c1a19;
    --ink-soft:#3a3431;
    --gold:#b57a2b;
    --gold-light:#c08a3e;
    --cream:#f2eee8;
  }
  *{box-sizing:border-box;margin:0;padding:0}
  html,body{width:1187px;height:1200px;overflow:hidden;background:var(--page)}
  .label{
    position:absolute;left:151px;top:50px;width:884px;height:1100px;
    display:flex;box-shadow:0 2px 10px rgba(0,0,0,.12);
  }
  .brand-band{
    position:relative;width:302px;height:100%;background:var(--roast);overflow:hidden;
  }
  .brand-main,.brand-sub{
    position:absolute;
    writing-mode:vertical-rl;
    transform:translateX(-50%) rotate(180deg);
    text-align:center;white-space:nowrap;line-height:1;
    font-family:"Cormorant SC",serif;
  }
  .brand-main{
    left:132px;top:69px;height:847px;
    font-size:116px;font-weight:600;letter-spacing:1px;color:var(--cream);
  }
  .brand-sub{
    left:222px;top:250px;height:470px;
    font-size:56px;font-weight:500;letter-spacing:12px;color:var(--gold-light);
  }
  .brand-rule{
    position:absolute;left:219px;width:3px;background:var(--gold);border-radius:2px;
  }
  .brand-rule.upper{top:77px;height:160px;background:linear-gradient(180deg,rgba(181,122,43,.1),var(--gold))}
  .brand-rule.lower{top:735px;height:55px;background:linear-gradient(180deg,var(--gold),rgba(181,122,43,.1))}
  .net-weight{
    position:absolute;left:94px;top:962px;width:160px;height:97px;
    background:var(--gold);border-radius:12px 12px 12px 0;
    display:flex;flex-direction:column;align-items:center;justify-content:center;
    font-family:"Lato",sans-serif;font-size:27px;line-height:1.15;color:#fff;
  }
  .blend-panel{
    position:relative;flex:1;height:100%;
    background:linear-gradient(160deg,#f1f1f3 0%,var(--paper) 55%,var(--paper-edge) 100%);
    padding:55px 40px 0 37px;
  }
  .blend-title{
    font-family:"Cormorant SC",serif;font-weight:700;color:var(--ink);
    font-size:100px;line-height:.98;letter-spacing:1px;white-space:nowrap;
  }
  .rule{
    height:5px;width:476px;
    background:linear-gradient(90deg,var(--gold) 0%,var(--gold) 55%,rgba(181,122,43,.15) 100%);
    border-radius:3px;
  }
  .rule.first{margin-top:106px}
  .blend-copy{
    font-family:"Cormorant SC",serif;font-weight:600;color:var(--ink-soft);
    font-size:38px;line-height:1.05;padding:16px 0 16px 2px;white-space:nowrap;
  }
</style>
</head>
<body>
  <main class="label">
    <section class="brand-band">
      <div class="brand-main">Willow Ridge</div>
      <span class="brand-rule upper"></span>
      <div class="brand-sub">Coffee Co.</div>
      <span class="brand-rule lower"></span>
      <div class="net-weight"><span>Net Wt.</span><span>16 oz.</span></div>
    </section>
    <section class="blend-panel">
      <h1 class="blend-title">Long Drive<br>Blend</h1>
      <div class="rule first"></div>
      <p class="blend-copy">Notes: Balanced, carmelly<br>sweet, espresso strength</p>
      <div class="rule"></div>
      <p class="blend-copy">Perfect for use as an<br>espresso, or on it’s own.<br>Compliments your daily<br>commute or road trip</p>
      <div class="rule"></div>
    </section>
  </main>
</body>
</html>
```